Re-vamp existing website :www.tallowmerefinch.com.au

We need a new website design for this website
www.tallowmerefinch.com.au.

"sparking bright financial ideas"

Looking for something modern, corporate like this https://www.pebbleharbor.com.au

Imagery is important, showing really great images of what we do.

We want to keep the theme of:
Build Your Future
Invest in your Dreams
Grow You

We want a blog/opinion page on the website

Staying with our three logo colours throughout

Industry/Entity Type

Financial Service

Number of Pages Required

5+ page

```html
<!DOCTYPE html>
<html lang="en">
<head>
<meta charset="utf-8">
<title>Tallowmere Finch – Home</title>
<link rel="stylesheet" href="https://fonts.googleapis.com/css2?family=Kanit:wght@300;400;500&family=Open+Sans:wght@400;600;700&display=swap">
<style>
:root{
  --blue:#1d9bd7;
  --blue-deep:#1287c4;
  --blue-btn:#3a84d8;
  --green:#a6c93a;
  --green-btn:#9ac43a;
  --ink:#222;
  --text:#555;
  --grey-band:#efefef;
  --grey-line:#d8d8d8;
  --footer:#f2f2f2;
  --white:#fff;
}
*{box-sizing:border-box;margin:0;padding:0}
html,body{width:1200px;height:2535px;overflow:hidden}
body{position:relative;background:var(--white);font-family:"Open Sans",Arial,sans-serif;color:var(--text)}

/* header */
.site-header{position:absolute;left:0;top:0;width:1200px;height:97px;background:var(--white)}
.brand{position:absolute;left:60px;top:18px;display:flex;align-items:center;gap:12px}
.brand-dot{width:44px;height:44px;border-radius:50%;background:var(--blue)}
.brand-name{font-family:"Kanit",Arial,sans-serif;font-weight:500;font-size:28px;color:var(--blue);line-height:1}
.brand-tagline{position:absolute;left:116px;top:62px;font-family:"Kanit",Arial,sans-serif;font-size:13px;color:var(--blue);white-space:nowrap}
.contact-item{position:absolute;top:34px;display:flex;gap:12px;align-items:center}
.contact-item svg{width:28px;height:28px}
.contact-item strong{display:block;font-size:15px;color:var(--ink);font-weight:600}
.contact-item span{display:block;font-size:14px;color:var(--text)}
.contact-phone{left:660px}
.contact-hours{left:930px}

/* hero */
.hero{position:absolute;left:0;top:97px;width:1200px;height:511px;background:linear-gradient(120deg,#27a4dc 0%,#1b96d3 55%,#2aa6dd 100%)}
.hero-title{position:absolute;top:118px;width:100%;text-align:center;font-family:"Kanit",Arial,sans-serif;font-weight:400;font-size:42px;color:var(--white)}
.step{position:absolute;top:217px;width:210px;text-align:center}
.step-box{height:174px;border:1px solid rgba(255,255,255,.75);display:flex;align-items:center;justify-content:center}
.step-box svg{width:110px;height:90px}
.step-label{margin-top:22px;font-size:16px;color:var(--white);font-weight:600}

/* nav */
.main-nav{position:absolute;left:0;top:608px;width:1200px;height:64px;background:#f1f1f1}
.nav-dot{position:absolute;left:84px;top:14px;width:36px;height:36px;border-radius:50%;background:var(--blue)}
.nav-links{position:absolute;left:310px;top:0;display:flex;height:64px;list-style:none}
.nav-links li{padding:0 18px;line-height:64px;font-family:"Kanit",Arial,sans-serif;font-weight:300;font-size:15px;color:var(--ink);position:relative}
.nav-links li.is-active::after{content:"";position:absolute;left:6px;right:6px;bottom:0;height:4px;background:var(--green)}

/* intro */
.intro{position:absolute;left:0;top:672px;width:1200px;height:423px}
.intro h1{position:absolute;left:86px;top:58px;font-family:"Kanit",Arial,sans-serif;font-weight:400;font-size:58px;color:var(--ink);letter-spacing:.2px}
.intro p{position:absolute;left:90px;width:1022px;font-size:15px;line-height:23px;color:var(--text)}
.intro .p1{top:158px}
.intro .p2{top:244px}
.cta{position:absolute;left:88px;top:324px;width:308px;height:53px;background:var(--green-btn);border-radius:4px;color:var(--white);font-size:13px;display:flex;align-items:center;justify-content:center;text-transform:uppercase;letter-spacing:.3px}

/* lenders */
.lenders{position:absolute;left:0;top:1095px;width:1200px;height:387px;background:var(--grey-band)}
.lenders h2{position:absolute;left:82px;top:48px;font-family:"Kanit",Arial,sans-serif;font-weight:400;font-size:30px;color:var(--blue)}
.lender-grid{position:absolute;left:83px;top:125px;display:grid;grid-template-columns:repeat(6,152px);column-gap:27px;row-gap:22px}
.lender-card{height:80px;background:var(--white);border:1px solid var(--grey-line);border-radius:3px;display:flex;align-items:center;justify-content:center}
.lender-mark{width:108px;height:34px;border-radius:3px;background:#c9c9c9}

/* services */
.services{position:absolute;left:0;top:1570px;width:1200px}
.service{position:absolute;top:0;width:243px}
.service-photo{height:172px}
.service-label{height:45px;background:var(--blue);color:var(--white);font-family:"Kanit",Arial,sans-serif;font-size:20px;display:flex;align-items:center;justify-content:center}

/* signup */
.signup{position:absolute;left:0;top:1911px;width:1200px;height:364px;background:var(--green)}
.signup-dot{position:absolute;left:556px;top:-44px;width:88px;height:88px;border-radius:50%;background:var(--blue)}
.signup h2{position:absolute;top:122px;width:100%;text-align:center;font-family:"Kanit",Arial,sans-serif;font-weight:500;font-size:38px;color:var(--white)}
.signup p{position:absolute;top:184px;left:340px;width:520px;text-align:center;font-size:15px;line-height:22px;color:var(--white)}
.btn-signup{position:absolute;left:399px;top:261px;width:184px;height:39px;background:var(--blue-btn);color:var(--white);font-size:12px;font-weight:700;display:flex;align-items:center;justify-content:center;gap:6px}
.btn-login{position:absolute;left:592px;top:261px;width:183px;height:39px;border:1px solid #4f6a1b;color:#334514;font-size:12px;display:flex;align-items:center;justify-content:center}

/* footer */
.site-footer{position:absolute;left:0;top:2275px;width:1200px;height:260px;background:var(--footer);text-align:center}
.social{position:absolute;left:522px;top:58px;display:flex;gap:10px}
.social span{width:30px;height:30px;background:#555;transform:rotate(45deg);margin:6px}
.footer-links{position:absolute;top:128px;width:100%;display:flex;justify-content:center;gap:26px;list-style:none;font-family:"Kanit",Arial,sans-serif;font-weight:300;font-size:12px;color:var(--ink)}
.copyright{position:absolute;top:172px;width:100%;font-size:12px;color:var(--text)}
.terms{position:absolute;top:195px;width:100%;font-size:12px;color:var(--text)}
</style>
</head>
<body>

<header class="site-header">
  <div class="brand"><div class="brand-dot"></div><div class="brand-name">tallowmerefinch</div></div>
  <div class="brand-tagline">sparking bright financial ideas</div>
  <div class="contact-item contact-phone">
    <svg viewBox="0 0 28 28"><path d="M7 4l4 5-2 3c1.5 3 4 5.5 7 7l3-2 5 4-2 4C14 25 3 14 3 6z" fill="none" stroke="#a6c93a" stroke-width="2" stroke-linejoin="round"/></svg>
    <div><strong>0400 555 019</strong><span>info@tallowmerefinch.com.au</span></div>
  </div>
  <div class="contact-item contact-hours">
    <svg viewBox="0 0 28 28"><circle cx="14" cy="14" r="11" fill="none" stroke="#a6c93a" stroke-width="2"/><path d="M14 7v7h5" fill="none" stroke="#a6c93a" stroke-width="2"/></svg>
    <div><strong>7:30 AM - 7:30 PM</strong><span>Monday to Saturday</span></div>
  </div>
</header>

<section class="hero" role="img" aria-label="Blue-tinted background photo of a team meeting">
  <h2 class="hero-title">How your TMF journey works...</h2>
  <div class="step" style="left:114px">
    <div class="step-box">
      <svg viewBox="0 0 110 90"><path d="M8 40l28-10 30 10 30-10v44l-30 10-30-10-28 10z" fill="none" stroke="#fff" stroke-width="5" stroke-linejoin="round"/><path d="M36 30v44M66 40v44" stroke="#fff" stroke-width="5"/><circle cx="80" cy="20" r="11" fill="none" stroke="#fff" stroke-width="5"/><path d="M71 26l9 20 9-20" fill="#fff"/></svg>
    </div>
    <div class="step-label">Our TMF Mapping Session</div>
  </div>
  <div class="step" style="left:366px">
    <div class="step-box">
      <svg viewBox="0 0 110 90"><circle cx="55" cy="14" r="9" fill="#fff"/><rect x="44" y="24" width="22" height="16" rx="4" fill="#fff"/><path d="M55 40v10M20 50h70M20 50v10M55 50v10M90 50v10" stroke="#fff" stroke-width="5" fill="none"/><rect x="8" y="60" width="24" height="22" fill="none" stroke="#fff" stroke-width="5"/><rect x="43" y="60" width="24" height="22" fill="none" stroke="#fff" stroke-width="5"/><rect x="78" y="60" width="24" height="22" fill="none" stroke="#fff" stroke-width="5"/></svg>
    </div>
    <div class="step-label">Structure &amp; Strategy</div>
  </div>
  <div class="step" style="left:620px">
    <div class="step-box">
      <svg viewBox="0 0 110 90"><path d="M38 38V26a17 17 0 0 1 34 0v12" fill="none" stroke="#fff" stroke-width="8"/><rect x="26" y="38" width="58" height="46" rx="5" fill="#fff"/><circle cx="55" cy="56" r="6" fill="#1d9bd7"/><rect x="52" y="58" width="6" height="14" fill="#1d9bd7"/></svg>
    </div>
    <div class="step-label">Protect</div>
  </div>
  <div class="step" style="left:872px">
    <div class="step-box">
      <svg viewBox="0 0 110 90"><path d="M25 45a30 30 0 0 1 52-20" fill="none" stroke="#fff" stroke-width="7"/><path d="M85 45a30 30 0 0 1-52 20" fill="none" stroke="#fff" stroke-width="7"/><path d="M70 14l12 12-16 4z" fill="#fff"/><path d="M40 76l-12-12 16-4z" fill="#fff"/><circle cx="55" cy="45" r="13" fill="#fff"/><circle cx="55" cy="45" r="5" fill="#1d9bd7"/></svg>
    </div>
    <div class="step-label">Implementation &amp; Review</div>
  </div>
</section>

<nav class="main-nav">
  <div class="nav-dot"></div>
  <ul class="nav-links">
    <li class="is-active">HOME</li>
    <li>ABOUT US</li>
    <li>MEET ROWAN</li>
    <li>HOME LOAN</li>
    <li>BUSINESS LENDING</li>
    <li>CONTACT US</li>
  </ul>
</nav>

<section class="intro">
  <h1>How your TMF journey works...</h1>
  <p class="p1">Tallowmere Finch (TMF) is a leading Australian finance brokerage group dedicated in providing our clients with a range of financial solutions tailored to their individual requirements.&nbsp; We want our clients to be bold in chasing their financial dreams and we commit to provide a range of opportunities for them to do so.</p>
  <p class="p2">Tallowmere Finch aims to push the status quo by doing things differently. We want you to start thinking bigger and we can show you the steps to get you there. We know you have your vision of where you want to be, we will provide the guidance you might need in getting there.</p>
  <div class="cta">Click here to start your journey!</div>
</section>

<section class="lenders">
  <h2>SUPPORT BUSINESS LENDING</h2>
  <div class="lender-grid">
    <div class="lender-card"><div class="lender-mark"></div></div>
    <div class="lender-card"><div class="lender-mark"></div></div>
    <div class="lender-card"><div class="lender-mark"></div></div>
    <div class="lender-card"><div class="lender-mark"></div></div>
    <div class="lender-card"><div class="lender-mark"></div></div>
    <div class="lender-card"><div class="lender-mark"></div></div>
    <div class="lender-card"><div class="lender-mark"></div></div>
    <div class="lender-card"><div class="lender-mark"></div></div>
    <div class="lender-card"><div class="lender-mark"></div></div>
    <div class="lender-card"><div class="lender-mark"></div></div>
    <div class="lender-card"><div class="lender-mark"></div></div>
    <div class="lender-card"><div class="lender-mark"></div></div>
  </div>
</section>

<section class="services">
  <div class="service" style="left:60px">
    <div class="service-photo" role="img" aria-label="Photo of moving boxes stacked in an open field under a cloudy sky" style="background:linear-gradient(180deg,#a9b3b8,#8c7a62)"></div>
    <div class="service-label">First Home Buyer</div>
  </div>
  <div class="service" style="left:338px">
    <div class="service-photo" role="img" aria-label="Photo of hands holding a phone and a bank card" style="background:linear-gradient(180deg,#4f6f8c,#243246)"></div>
    <div class="service-label">Next Home Buyers</div>
  </div>
  <div class="service" style="left:619px">
    <div class="service-photo" role="img" aria-label="Photo of a man working on a tablet at a desk" style="background:linear-gradient(180deg,#e3e6e4,#7a8a8c)"></div>
    <div class="service-label">Refinancing</div>
  </div>
  <div class="service" style="left:899px">
    <div class="service-photo" role="img" aria-label="Photo of a woman reading a tablet on a sofa" style="background:linear-gradient(180deg,#d8cfc4,#8a6f58)"></div>
    <div class="service-label">Investment</div>
  </div>
</section>

<section class="signup">
  <div class="signup-dot"></div>
  <h2>Sign up for Tallowmerefinch</h2>
  <p>At Tallowmere Finch our team is on the road everyday and we're able to come to you at your preferred location.</p>
  <div class="btn-signup"><svg width="10" height="12" viewBox="0 0 10 12"><path d="M2.5 5V3.5a2.5 2.5 0 0 1 5 0V5" fill="none" stroke="#fff" stroke-width="1.5"/><rect x="1" y="5" width="8" height="7" rx="1" fill="#fff"/></svg>SIGN UP FREE</div>
  <div class="btn-login">LOG IN</div>
</section>

<footer class="site-footer">
  <div class="social"><span></span><span></span><span></span><span></span></div>
  <ul class="footer-links">
    <li>HOME</li><li>ABOUT US</li><li>MEET ROWAN</li><li>HOME LOAN</li><li>BUSINESS LENDING</li><li>CONTACT US</li>
  </ul>
  <div class="copyright">© 2017 tallowmerefinch, Inc. All rights reserved.</div>
  <div class="terms">Terms, conditions, features, availability, pricing, fees, service and support options subject to change without notice.</div>
</footer>

</body>
</html>
```